Camp Thornbrook 2021 Magazine Design

We are for someone to design our annual magazine/newsletter. This is a print newsletter that is a total of 20 pages. It will need to be designed in a way that is easy to share with our printers. The designer will need to be someone who is creative and easy to work with.
For those interested in this project we ask that you design 4 to 6 pages for us to view. Once we select the designer we will want the rest created in a two-week time span. For those submitting a bid please include front cover, theme & dates, mission & vision, and Lend a Hand Forward.

This link will provide the layout of the newsletter https://files.pelmarsh.example/doc/7qTzR2kLpW9xVbN4cHsYd/view.

This link will provide you with the pictures that are needed and a few documents https://files.pelmarsh.example/folder/3hGvK8mQxZ5rLtP1wNcBj/view

Details:
20 pages long (including covers)
8.5 x 11

Please message me if you need any further details.

Target Market(s)

Our alumni base. Covers all ages

Requirements
Must have
• Spelled out in document
Nice to have
• Spelled out in document
Should not have
• Spelled out in document

```html
<!DOCTYPE html>
<html lang="en">
<head>
<meta charset="utf-8">
<title>Camp Thornbrook — Resurrection 2021 Spread</title>
<link href="https://fonts.googleapis.com/css2?family=Questrial&family=Josefin+Sans:wght@300;400&family=Tinos&display=swap" rel="stylesheet">
<style>
  :root {
    --backdrop: #bf8e87;
    --paper: #ffffff;
    --ink: #1e1e1e;
    --forest: #1f3527;
    --footer-orange: #e8915a;
    --session-yellow: #f0cf1c;
    --date-blue: #9fb8da;
    --price-orange: #d9622b;
    --panel-orange: #f2b76b;
    --age-orange: #f0a95a;
    --age-border: #f5c542;
    --photo-dark: #2b2b2b;
    --photo-mid: #6f6f6f;
    --photo-light: #bdbdbd;
    --moon-gray: #7a7a7a;
  }
  * { box-sizing: border-box; margin: 0; padding: 0; }
  html, body { width: 1200px; height: 900px; overflow: hidden; }
  body { background: var(--backdrop); font-family: "Questrial", sans-serif; color: var(--ink); position: relative; }

  .spread { position: absolute; left: 60px; top: 90px; width: 1080px; height: 720px; display: flex; box-shadow: 0 18px 40px rgba(0,0,0,.25); }
  .page { position: relative; width: 540px; height: 720px; background: var(--paper); overflow: hidden; }
  .page--left { border-radius: 14px 0 0 4px; }
  .page--right { border-radius: 0 4px 4px 0; }

  /* Left page cover art */
  .cover-photo { position: absolute; left: 0; top: 0; width: 540px; height: 558px; border-radius: 14px 0 0 0;
    background: linear-gradient(180deg, var(--photo-light) 0%, var(--photo-mid) 45%, var(--photo-dark) 100%); }
  .cover-shapes { position: absolute; left: 0; top: 0; }
  .cover-title { position: absolute; left: 0; width: 540px; top: 222px; text-align: center;
    font-family: "Josefin Sans", sans-serif; font-weight: 400; font-size: 60px; letter-spacing: 3px;
    color: transparent; -webkit-text-stroke: 1.6px #ffffff; }
  .cover-quote { position: absolute; left: 196px; top: 300px; width: 318px; text-align: right;
    font-family: "Tinos", serif; font-size: 11.5px; line-height: 1.35; color: #ffffff; }
  .cover-year { position: absolute; left: 294px; top: 348px; width: 120px; text-align: center;
    font-family: "Josefin Sans", sans-serif; font-size: 40px; letter-spacing: 2px;
    color: transparent; -webkit-text-stroke: 1.3px #ffffff; }

  .registration { position: absolute; left: 28px; top: 586px; width: 330px; }
  .registration h2 { font-size: 15px; font-weight: 700; margin-bottom: 5px; }
  .registration ul { list-style: none; font-size: 11px; line-height: 1.35; }
  .registration li::before { content: "• "; }

  .camp-mark { position: absolute; left: 364px; top: 572px; display: flex; align-items: center; gap: 8px; }
  .camp-mark__dot { width: 34px; height: 34px; border-radius: 50%; background: var(--forest); }
  .camp-mark__name { font-size: 16px; color: var(--forest); line-height: 1.1; }

  .page-footer { position: absolute; left: 0; bottom: 0; width: 540px; height: 22px; display: flex; font-size: 11px; }
  .page-footer__title { flex: 1; background: var(--forest); color: #ffffff; padding: 5px 0 0 22px; }
  .page-footer__number { width: 126px; background: var(--footer-orange); color: var(--ink); text-align: center; padding-top: 5px; }

  /* Right page */
  .sessions-title { position: absolute; left: 20px; top: 24px; font-size: 15px; font-weight: 700; }
  .schedule { position: absolute; top: 47px; left: 14px; display: flex; gap: 8px; }
  .schedule__col { width: 164px; height: 228px; padding: 8px 8px; list-style: none; font-size: 11.5px; line-height: 22px; border-radius: 10px 10px 0 0; }
  .schedule__col--sessions { background: var(--session-yellow); }
  .schedule__col--dates { background: var(--date-blue); width: 158px; }
  .schedule__col--prices { background: var(--price-orange); width: 158px; border-radius: 10px 10px 10px 0; color: #3a1a0a; }

  .activities-panel { position: absolute; left: 4px; top: 276px; width: 536px; height: 422px; background: var(--panel-orange); border-radius: 16px 0 0 0; }
  .activities-panel h2 { position: absolute; left: 22px; top: 16px; width: 340px; font-size: 14px; font-weight: 700; line-height: 1.3; }
  .activity-list { position: absolute; left: 28px; top: 70px; font-size: 11.5px; line-height: 15.5px; padding-left: 26px; }

  .age-groups { position: absolute; left: 270px; top: 96px; width: 190px; height: 156px;
    background: var(--age-orange); border: 3px solid var(--age-border); border-radius: 16px; padding: 40px 0 0 20px; }
  .age-groups table { border-collapse: collapse; font-size: 14px; font-weight: 700; }
  .age-groups th { text-align: left; font-weight: 700; padding-right: 18px; }
  .age-groups td { padding-right: 18px; line-height: 18px; }
</style>
</head>
<body>
<main class="spread">
  <section class="page page--left">
    <div class="cover-photo" role="img" aria-label="Black and white photograph of a misty mountain ridge with trees"></div>
    <svg class="cover-shapes" width="540" height="558" viewBox="0 0 540 558" aria-hidden="true">
      <defs>
        <linearGradient id="sunsetGlow" x1="0" y1="0" x2="0" y2="1">
          <stop offset="0" stop-color="#f3d27a"/>
          <stop offset=".45" stop-color="#e98a5e"/>
          <stop offset="1" stop-color="#c24a7a"/>
        </linearGradient>
      </defs>
      <circle cx="226" cy="282" r="192" fill="url(#sunsetGlow)" role="img" aria-label="Sunset photograph inside circle"/>
      <circle cx="340" cy="257" r="190" fill="var(--moon-gray)" fill-opacity=".95"/>
    </svg>
    <h1 class="cover-title">RESURRECTION</h1>
    <p class="cover-quote">“Jesus said to her, “I am the resurrection and the life. The one who believes in me will live, even though they die;” John 11:25</p>
    <p class="cover-year">2021</p>

    <div class="registration">
      <h2>Registration and other information:</h2>
      <ul>
        <li>Registration begins on January 1, 2021</li>
        <li>Register online at campthornbrook.example</li>
        <li>Super Early Bird Discount ($20) if registered before April 1st</li>
        <li>Early Bird Discount ($10) if registered in the month of April</li>
      </ul>
    </div>
    <div class="camp-mark">
      <span class="camp-mark__dot"></span>
      <span class="camp-mark__name">Camp<br>Thornbrook</span>
    </div>

    <footer class="page-footer">
      <span class="page-footer__title">Resurrection 2021</span>
      <span class="page-footer__number">6</span>
    </footer>
  </section>

  <section class="page page--right">
    <h2 class="sessions-title">Sessions and Dates</h2>
    <div class="schedule">
      <ul class="schedule__col schedule__col--sessions">
        <li>Session 1</li><li>Short Session 1</li><li>Session 2</li><li>Session 2B</li><li>Session 3</li>
        <li>Session 3B</li><li>Session 4</li><li>Session 4B</li><li>Session 5</li><li>Short Session 2</li>
      </ul>
      <ul class="schedule__col schedule__col--dates">
        <li>May 30 - June 5</li><li>May 30 - June 2</li><li>June 6 - June 17</li><li>June 6 - June 12</li><li>June 27 - July 8</li>
        <li>June 27 - July 3</li><li>July 11 - July 22</li><li>July 11 - July 17</li><li>July 25 - July 31</li><li>July 25 - July 28</li>
      </ul>
      <ul class="schedule__col schedule__col--prices">
        <li>$265</li><li>$175</li><li>$425</li><li>$265</li><li>$425</li>
        <li>$265</li><li>$425</li><li>$265</li><li>$265</li><li>$175</li>
      </ul>
    </div>

    <div class="activities-panel">
      <h2>Activities (Put a few good clipart pictures of some activity examples above list of activities)</h2>
      <ul class="activity-list">
        <li>Archery Tag</li><li>Blob</li><li>Horseback Riding</li><li>Hiking</li><li>Gaga Ball</li>
        <li>Golden Goat (New)</li><li>Rappelling</li><li>Archery</li><li>Hatchet Throwing (New)</li>
        <li>Basketball</li><li>Arts and Crafts</li><li>9 Square in the Air</li><li>Swimming</li><li>And much more!</li>
      </ul>
      <div class="age-groups">
        <table>
          <tr><th>Group</th><th>Age</th></tr>
          <tr><td>1</td><td>8-10 Years</td></tr>
          <tr><td>2</td><td>11-12 Years</td></tr>
          <tr><td>3</td><td>13-14 Years</td></tr>
          <tr><td>4</td><td>15-18 Years</td></tr>
        </table>
      </div>
    </div>

    <footer class="page-footer">
      <span class="page-footer__title">Resurrection 2021</span>
      <span class="page-footer__number">7</span>
    </footer>
  </section>
</main>
</body>
</html>
```